Label design for one hand cream.

The name of the company is Olvu. We are launching a hand cream that is also an immediate cleaner without any water. It removes dirt from your hands without using water. After the use, your hands will be soft. It could be used in your feet too.

The company logo reminds of plants, nature and we would like this approach too. Please, remove the words "Produtos Naturais" from the logo.

Reason: Not enough designs. Bad ones

Reason: I have not received one design that pleased us.

Target Market(s)

Public in General. Mostly women.

Industry/Entity Type

Cosmetics

Font styles to use
Sans Serif

Colors
33b8a4
00a990
9bcb3c
acd036
fee087
fece3e
ffc214
fbed22
fbee3e

Requirements
Must have
• You must use the words in the label. Please, see the file attached but just use the WORDS, not the same structure. The image must be 15,5cm high and 7,5 cm wide.
• Use a darker green and some GOLDEN lines or details. You can even put the Logo plant on the golden color.
• "Velmire Plus"
• "Ação 3 em 1: Esfoliante, limpeza e hidratação"
• "Regeneração Celular"
• "Calm Veil"
• Logo of the company "Olvu" (attached).
• Please, REMOVE the words "Produtos Naturais" from the logo.
• Elegance and show softness.
• Something that reminds of nature or fresh.
Should not have
• Strong colors or many images that distract the information.

```html
<!DOCTYPE html>
<html lang="pt">
<head>
<meta charset="utf-8">
<title>Olvu – Velmire Plus label</title>
<link href="https://fonts.googleapis.com/css2?family=Playball&family=Montserrat:wght@400;600&family=Roboto+Condensed:wght@700&family=Open+Sans:wght@600&display=swap" rel="stylesheet">
<style>
  :root{
    --bg:#ececec;
    --night:#0d0f0c;
    --leaf-deep:#1f3a1c;
    --leaf:#3f7a35;
    --tag-green:#2c4a1f;
    --title-green:#2c4a1f;
    --paper:#ecebe8;
    --ink:#2a2a2a;
    --gold-dark:#b57d12;
    --gold:#e0a91f;
    --gold-light:#fee087;
    --logo-green:#8fc86a;
  }
  *{margin:0;padding:0;box-sizing:border-box}
  html,body{width:1200px;height:1137px;overflow:hidden;background:var(--bg)}
  .label{position:absolute;top:40px;height:1057px}
  .side{left:200px;width:230px}
  .front{left:430px;width:380px}
  .foliage{position:absolute;left:0;right:0;
    background:radial-gradient(circle at 30% 40%,var(--leaf-deep) 0,transparent 45%),
               radial-gradient(circle at 75% 70%,var(--leaf-deep) 0,transparent 40%),var(--night)}
  .foliage.top{top:0;height:232px}
  .foliage.bottom{top:835px;height:222px}
  .gold-band{position:absolute;left:0;right:0;
    background:linear-gradient(180deg,var(--gold-dark) 0%,var(--gold) 30%,var(--gold-light) 55%,var(--gold) 75%,var(--gold-dark) 100%)}
  .gold-band.upper{top:232px;height:73px}
  .gold-band.lower{top:780px;height:55px}
  .paper{position:absolute;left:0;right:0;top:305px;height:475px;background:var(--paper)}
  .side .paper{border-right:1px solid #d8d6d2}
  .usage{position:absolute;left:22px;right:22px;top:30px;font-family:'Open Sans',sans-serif;font-weight:600;
    font-size:9.5px;line-height:1.45;color:var(--ink)}
  .usage p{margin-bottom:14px}
  .claim-tag{position:absolute;left:252px;top:0;width:62px;height:460px;background:var(--tag-green);
    border-bottom:7px solid var(--gold);display:flex;justify-content:center;padding-top:18px}
  .claim-tag span{writing-mode:vertical-rl;font-family:'Montserrat',sans-serif;font-size:17px;letter-spacing:1.5px;
    line-height:1.3;color:var(--gold-light)}
  .product-name{position:absolute;left:0;right:0;top:470px;text-align:center;font-family:'Playball',cursive;
    font-size:46px;color:var(--title-green)}
  .benefit{position:absolute;left:0;right:0;top:528px;text-align:center;font-family:'Montserrat',sans-serif;
    font-size:19px;letter-spacing:3px;color:var(--ink)}
  .gold-rule{position:absolute;left:68px;right:48px;top:560px;height:2px;background:linear-gradient(90deg,var(--gold),var(--gold-light),var(--gold))}
  .line-name{position:absolute;left:0;right:0;top:568px;text-align:center;font-family:'Roboto Condensed',sans-serif;
    font-weight:700;font-size:46px;background:linear-gradient(180deg,var(--gold-light),var(--gold) 55%,var(--gold-dark));
    -webkit-background-clip:text;background-clip:text;color:transparent}
  .volume{position:absolute;left:0;right:0;top:650px;text-align:center;font-family:'Montserrat',sans-serif;
    font-size:12.5px;line-height:1.6;color:var(--ink)}
  .volume::before{content:"";display:block;width:48px;height:2px;background:var(--ink);margin:0 auto 6px}
  .brand{position:absolute;left:44px;top:866px;width:292px;height:104px;border:3px solid var(--gold);border-radius:8px;
    background:var(--night);display:flex;align-items:center;justify-content:center;gap:16px}
  .brand i{width:34px;height:34px;border-radius:50%;background:var(--gold)}
  .brand span{font-family:'Montserrat',sans-serif;font-weight:600;font-size:70px;line-height:1;color:var(--logo-green)}
</style>
</head>
<body>
  <section class="label side">
    <div class="foliage top" role="img" aria-label="Watercolour green leaves on black"></div>
    <div class="gold-band upper"></div>
    <div class="paper">
      <div class="usage">
        <p>Apply a small amount to dry hands and massage gently until the gel rolls away dirt.</p>
        <p>No water is needed. The formula cleans, exfoliates and leaves a soft veil of moisture on the skin. Suitable for hands and feet, at home or on the go.</p>
        <p>Botanical extracts help renew the skin surface and refresh tired hands after a long day.</p>
        <p>For external use only. Avoid contact with eyes. Keep out of reach of children.</p>
        <p>Store in a cool, dry place away from direct sunlight. Use within twelve months after opening.</p>
      </div>
    </div>
    <div class="gold-band lower"></div>
    <div class="foliage bottom" role="img" aria-label="Watercolour green leaves on black"></div>
  </section>

  <section class="label front">
    <div class="foliage top" role="img" aria-label="Watercolour green leaves on black"></div>
    <div class="gold-band upper"></div>
    <div class="paper"></div>
    <div class="claim-tag"><span>AÇÃO 3 EM 1: ESFOLIANTE,<br>MÁSCARA E LIMPEZA</span></div>
    <h1 class="product-name">Velmire Plus</h1>
    <p class="benefit">Regeneração Celular</p>
    <div class="gold-rule"></div>
    <h2 class="line-name">Calm Veil</h2>
    <p class="volume">1.4 FL OZ<br>40 ML</p>
    <div class="gold-band lower"></div>
    <div class="foliage bottom" role="img" aria-label="Watercolour green leaves on black"></div>
    <div class="brand"><i></i><span>Olvu</span></div>
  </section>
</body>
</html>
```